Beacon Advisory Website

I currently have a website www.beaconadvisoryinc.example. We are a IT Consulting Company. Our website will pretty much tell out our services. I am looking to enhance my website and make it look more professional. Looking for very classy and Contemporary look and design for my website.

Industry/Entity Type

It Company

```html
<!DOCTYPE html>
<html lang="en">
<head>
<meta charset="utf-8">
<title>Beacon Advisory</title>
<link href="https://fonts.googleapis.com/css2?family=Montserrat:wght@400;500;600;700&family=Raleway:wght@500;600;700&display=swap" rel="stylesheet">
<style>
:root{
  --blue:#1f5fa8;
  --blue-dark:#173f73;
  --blue-bright:#1f85c8;
  --teal:#1b8fc4;
  --navy:#0f2a3c;
  --ink:#333d47;
  --muted:#6b7480;
  --light:#f4f4f4;
  --white:#ffffff;
  --line:#d6dbe0;
}
*{box-sizing:border-box;margin:0;padding:0}
html,body{width:1200px;height:3203px;overflow:hidden}
body{font-family:"Montserrat",Arial,sans-serif;color:var(--ink);background:var(--white);position:relative}
.section{position:absolute;left:0;width:1200px}
.wrap{position:relative;width:854px;margin:0 auto;height:100%}

/* top bar */
.topbar{top:0;height:36px;background:var(--blue);color:#fff;font-size:11px}
.topbar .info{position:absolute;right:168px;top:11px;display:flex;gap:26px;align-items:center}
.topbar .social{position:absolute;right:168px;top:12px;display:flex;gap:5px}
.topbar .info span{display:flex;align-items:center;gap:6px}
.dot{width:11px;height:11px;border-radius:50%;background:#fff;opacity:.9;display:inline-block}

/* header + hero */
.hero{top:36px;height:540px;background:linear-gradient(135deg,#cfe0ee 0%,#9fb9d3 35%,#6f8aa8 60%,#b9c8d6 100%)}
.hero .photo{position:absolute;inset:0;background:linear-gradient(180deg,rgba(240,245,250,.35),rgba(60,90,130,.25))}
.header{position:absolute;top:0;left:0;width:1200px;height:84px;background:rgba(255,255,255,.86)}
.logo{position:absolute;display:flex;align-items:center;gap:8px;font-weight:700;color:var(--blue);letter-spacing:.5px}
.logo .mark{width:26px;height:26px;background:var(--blue);border-radius:4px}
.header .logo{left:192px;top:26px;font-size:22px}
.nav{position:absolute;right:168px;top:34px;display:flex;gap:22px;font-size:12.5px;font-weight:600;color:var(--blue)}
.hero-caption{position:absolute;left:561px;top:164px;width:449px;padding:12px 22px;background:rgba(50,50,50,.78);color:#fff;font-size:25px;line-height:1.3;font-weight:500}
.dots{position:absolute;left:582px;top:504px;display:flex;gap:4px}
.dots i{width:9px;height:9px;border-radius:50%;background:#ddd;display:block}
.dots i:first-child{background:#999}

.band{top:576px;height:56px;background:var(--blue-dark);color:#fff}
.band .logo{left:0;top:14px;color:#fff;font-size:16px}
.band .logo .mark{background:#fff}
.band .tag{position:absolute;left:112px;top:11px;font-size:27px;font-weight:600}
.band .call{position:absolute;right:0;top:15px;display:flex;align-items:center;gap:14px;font-size:14px}
.band .call b{background:#fff;color:var(--blue-dark);padding:4px 14px;font-size:15px;font-weight:600;border-radius:2px;display:flex;gap:8px;align-items:center}

/* about */
.about{top:632px;height:326px;background:#fafafa;text-align:center}
.about .logo{left:372px;top:45px;color:#8a8f95;font-size:20px}
.about .logo .mark{background:#8a8f95}
.about p{position:absolute;left:173px;top:110px;width:854px;font-size:11.2px;line-height:2;color:var(--muted)}
.btn{display:inline-block;background:var(--blue);color:#fff;font-size:11px;font-weight:600;padding:6px 22px;border-radius:2px}
.about .btn{position:absolute;left:563px;top:213px}

/* cards */
.cards{top:958px;height:250px;background:#fff}
.card{position:absolute;top:0;width:271px;height:186px}
.card .img{position:absolute;inset:0}
.card .bar{position:absolute;left:0;bottom:0;width:100%;height:64px;background:rgba(22,55,105,.92);color:#fff;display:flex;align-items:center;gap:12px;padding-left:16px;font-size:15px;font-weight:600}
.card .bar svg{width:30px;height:30px}

/* services */
.services{top:1208px;height:496px;background:var(--light)}
.h2{position:absolute;left:0;width:100%;text-align:center;font-size:22px;font-weight:500;color:#444}
.services .h2{top:56px}
.svc{position:absolute;width:260px;display:flex;gap:16px}
.svc svg{flex:none;width:52px;height:56px}
.svc h3{font-size:15px;font-weight:600;color:var(--blue-bright);line-height:1.2;margin-top:6px}
.svc p{font-size:10.5px;color:var(--muted);line-height:1.7;margin-top:10px}

/* testimonials */
.testimonials{top:1704px;height:363px;background:var(--teal);color:#fff}
.testimonials .h2{top:58px;color:#fff;font-weight:600}
.quote{position:absolute;top:160px;display:flex;gap:30px}
.quote .photo{width:198px;height:137px}
.quote h4{font-size:15px;font-weight:600;margin-top:4px}
.quote .role{font-size:11px;font-weight:600;margin-top:4px}
.quote p{font-size:11px;line-height:1.55;width:190px;margin-top:10px;opacity:.95}

/* callback */
.callback{top:2067px;height:273px;background:var(--navy);color:#fff}
.callback .title{position:absolute;left:0;top:116px;display:flex;gap:22px;align-items:center}
.callback .title span{font-family:"Raleway",sans-serif;font-size:26px;font-weight:600;color:#c9d3dc;line-height:1.25}
.callback label{position:absolute;left:296px;top:72px;font-size:12px;color:#c9d3dc}
.field{position:absolute;height:37px;background:#fff;color:#666;font-size:12px;padding:11px 18px;border-radius:2px}
.submit{position:absolute;left:581px;top:160px;width:100px;height:37px;background:var(--blue);color:#fff;font-weight:700;font-size:14px;text-align:center;line-height:37px;border:1px solid #2d7bd0}

/* map */
.map{top:2340px;height:335px;background:linear-gradient(135deg,#eef0f2,#e2e5e8 60%,#dfe8ee)}

/* offices */
.offices{top:2675px;height:218px;background:var(--blue);color:#fff}
.office{position:absolute;top:55px;width:250px}
.office h4{font-size:17px;font-weight:700;margin-bottom:22px}
.office .row{display:flex;gap:14px;font-size:11px;line-height:1.5;margin-bottom:16px}
.office .row svg{flex:none;width:12px;height:14px;margin-top:1px}
.divider{position:absolute;top:55px;width:1px;height:110px;background:rgba(255,255,255,.35)}

/* footer */
.footer{top:2893px;height:256px;background:var(--blue);border-top:1px solid rgba(255,255,255,.2);color:#fff}
.footer .logo{left:0;top:44px;color:#b9c9dd;font-size:20px}
.footer .logo .mark{background:#b9c9dd}
.footer .about-text{position:absolute;left:0;top:102px;width:200px;font-size:11px;line-height:1.55}
.fcol{position:absolute;top:60px;width:185px}
.fcol h5{font-size:12px;font-weight:700;padding-bottom:12px;border-bottom:1px solid rgba(255,255,255,.3);margin-bottom:14px}
.fcol ul{list-style:none;font-size:11px;line-height:1.5}
.fcol li::before{content:"›";margin-right:8px}
.fcol p{font-size:11px;line-height:1.5}
.subscribe{display:flex;margin-top:4px}
.subscribe span{width:152px;height:28px;background:#fff;color:#777;font-size:11px;padding:7px 10px}
.subscribe b{width:26px;height:28px;background:#4fa6e0}

.copy{top:3149px;height:54px;background:var(--blue);border-top:1px solid rgba(255,255,255,.2);color:#fff;font-size:11px}
.copy .text{position:absolute;left:16px;top:20px}
.copy .icons{position:absolute;right:0;top:13px;display:flex;gap:6px}
.copy .icons i{width:26px;height:26px;border-radius:50%;background:#fff;display:block}
</style>
</head>
<body>

<div class="section topbar">
  <div class="info">
    <span><svg width="9" height="11" viewBox="0 0 10 13"><path d="M5 0a4.5 4.5 0 0 0-4.5 4.5C.5 8 5 13 5 13s4.5-5 4.5-8.5A4.5 4.5 0 0 0 5 0zm0 6.3a1.8 1.8 0 1 1 0-3.6 1.8 1.8 0 0 1 0 3.6z" fill="#fff"/></svg>48 Harbor Ave Suite 120 Eastfield, NJ 07000</span>
    <span><svg width="10" height="10" viewBox="0 0 12 12"><path d="M2.5 0l2 2.5-1.2 1.5a8 8 0 0 0 4.7 4.7L9.5 7.5 12 9.5 10.5 12C4.5 12 0 7.5 0 1.5z" fill="#fff"/></svg>+1 (555) 014 2200</span>
    <span style="gap:5px"><i class="dot"></i><i class="dot"></i><i class="dot"></i><i class="dot"></i></span>
  </div>
</div>

<div class="section hero">
  <div class="photo" role="img" aria-label="Photo of a consultant presenting charts on a glass board to a team seated around a meeting table"></div>
  <div class="header">
    <div class="logo"><span class="mark"></span>Beacon Advisory</div>
    <nav class="nav"><span>Company</span><span>Services</span><span>Solutions</span><span>Resources</span><span>Career</span><span>Contact Us</span></nav>
  </div>
  <div class="hero-caption">Delivers highest level of Quality Consultants and services</div>
  <div class="dots"><i></i><i></i><i></i></div>
</div>

<div class="section band">
  <div class="wrap">
    <div class="logo"><span class="mark"></span>Beacon</div>
    <div class="tag">24x7</div>
    <div class="call">Call us today for enquiry <b><svg width="12" height="12" viewBox="0 0 12 12"><path d="M2.5 0l2 2.5-1.2 1.5a8 8 0 0 0 4.7 4.7L9.5 7.5 12 9.5 10.5 12C4.5 12 0 7.5 0 1.5z" fill="#173f73"/></svg>+1 (555) 014 2200</b></div>
  </div>
</div>

<div class="section about">
  <div class="logo"><span class="mark"></span>Beacon Advisory</div>
  <p>Today's IT market is a dynamic, fast-paced industry, with ever-increasing demands. Meeting these demands for over 25 years, Beacon Advisory maintains a global presence, aggressively recruiting expertly qualified IT and Management Professionals from around the world and cultivating key partnerships with corporations to understand their business models end to end, with a goal of delivering exceptional client service and ensuring a consistent delivery of the talent needed to drive results.</p>
  <span class="btn">Read more</span>
</div>

<div class="section cards">
  <div class="card" style="left:173px">
    <div class="img" role="img" aria-label="Photo of hands working over documents and charts" style="background:linear-gradient(135deg,#e4edf5,#a9c3dd)"></div>
    <div class="bar"><svg viewBox="0 0 30 30"><path d="M3 14l6-5 6 3 6-3 6 5-8 7-4-3-4 3z" fill="#fff"/></svg>Consulting</div>
  </div>
  <div class="card" style="left:465px">
    <div class="img" role="img" aria-label="Photo of a smiling business team" style="background:linear-gradient(135deg,#6a9bd0,#cfd8e0)"></div>
    <div class="bar"><svg viewBox="0 0 30 30"><circle cx="15" cy="9" r="5" fill="#fff"/><path d="M6 26a9 9 0 0 1 18 0z" fill="#fff"/><circle cx="7" cy="12" r="3" fill="#fff"/><circle cx="23" cy="12" r="3" fill="#fff"/></svg>Staff Augmentation</div>
  </div>
  <div class="card" style="left:758px">
    <div class="img" role="img" aria-label="Photo of an offshore oil platform at sea" style="background:linear-gradient(180deg,#5d8cc7,#9ab7d9 60%,#3f6290)"></div>
    <div class="bar"><svg viewBox="0 0 30 30"><circle cx="15" cy="15" r="11" fill="none" stroke="#fff" stroke-width="4"/><circle cx="15" cy="15" r="4" fill="#fff"/></svg>Offshore</div>
  </div>
</div>

<div class="section services">
  <div class="h2">Our Services</div>
  <div class="svc" style="left:181px;top:140px">
    <svg viewBox="0 0 52 56"><path d="M26 2l22 12v28L26 54 4 42V14z" fill="none" stroke="#1f5fa8" stroke-width="2.5"/><circle cx="26" cy="28" r="9" fill="#1f85c8"/></svg>
    <div><h3>Technology</h3><p>Beacon Advisory Training programs are perfect for individuals</p></div>
  </div>
  <div class="svc" style="left:474px;top:140px">
    <svg viewBox="0 0 52 56"><path d="M26 2l22 12v28L26 54 4 42V14z" fill="none" stroke="#1f5fa8" stroke-width="2.5"/><rect x="16" y="22" width="20" height="14" rx="2" fill="#1f85c8"/><rect x="22" y="18" width="8" height="5" fill="none" stroke="#1f85c8" stroke-width="2"/></svg>
    <div><h3>Business</h3><p>Our Offshore development model has a unique distinction</p></div>
  </div>
  <div class="svc" style="left:769px;top:140px">
    <svg viewBox="0 0 52 56"><path d="M26 2l22 12v28L26 54 4 42V14z" fill="none" stroke="#1f5fa8" stroke-width="2.5"/><circle cx="26" cy="28" r="8" fill="none" stroke="#1f85c8" stroke-width="4" stroke-dasharray="4 2"/><circle cx="26" cy="28" r="3" fill="#1f85c8"/></svg>
    <div><h3>Application<br>Development</h3><p>Drawing on our experience in all major industries, we develop</p></div>
  </div>
  <div class="svc" style="left:181px;top:313px">
    <svg viewBox="0 0 52 56"><path d="M26 2l22 12v28L26 54 4 42V14z" fill="none" stroke="#1f5fa8" stroke-width="2.5"/><circle cx="26" cy="28" r="10" fill="#1f85c8"/><circle cx="26" cy="28" r="4" fill="#fff"/></svg>
    <div><h3>Enterprise<br>Integration</h3><p>As organizations work to achieve and sustain competitive</p></div>
  </div>
  <div class="svc" style="left:474px;top:313px">
    <svg viewBox="0 0 52 56"><path d="M26 2l22 12v28L26 54 4 42V14z" fill="none" stroke="#1f5fa8" stroke-width="2.5"/><rect x="15" y="19" width="22" height="15" rx="1" fill="none" stroke="#1f85c8" stroke-width="3"/><rect x="12" y="35" width="28" height="3" fill="#1f85c8"/></svg>
    <div><h3>IT Consulting</h3><p>Information technology should improve business results</p></div>
  </div>
  <div class="svc" style="left:769px;top:313px">
    <svg viewBox="0 0 52 56"><path d="M26 2l22 12v28L26 54 4 42V14z" fill="none" stroke="#1f5fa8" stroke-width="2.5"/><circle cx="26" cy="28" r="10" fill="none" stroke="#1f85c8" stroke-width="2"/><circle cx="26" cy="28" r="6" fill="none" stroke="#1f85c8" stroke-width="2"/><circle cx="26" cy="28" r="2" fill="#1f85c8"/></svg>
    <div><h3>Research</h3><p>we're helping you solve your business challenges today</p></div>
  </div>
</div>

<div class="section testimonials">
  <div class="h2">Testimonials</div>
  <div class="quote" style="left:173px">
    <div class="photo" role="img" aria-label="Portrait photo of Adrian Keller" style="background:linear-gradient(135deg,#e8ecef,#9aa7b3)"></div>
    <div><h4>Adrian Keller</h4><div class="role">CEO &amp; MD</div><p>Lorem ipsum dolor sit amet, tetuer adipiscing elit, sed diam nonummy nibh euismod tincidunt ut laoreet dolore magna aliquam erat lutpat.</p></div>
  </div>
  <div class="quote" style="left:611px">
    <div class="photo" role="img" aria-label="Portrait photo of Helena Morrow" style="background:linear-gradient(135deg,#8c7350,#4a3f33)"></div>
    <div><h4>Helena Morrow</h4><div class="role">Managing Director</div><p>Lorem ipsum dolor sit amet, tetuer adipiscing elit, sed diam nonummy nibh euismod tincidunt ut laoreet dolore magna aliquam erat lutpat.</p></div>
  </div>
</div>

<div class="section callback">
  <div class="wrap">
    <div class="title">
      <svg width="56" height="60" viewBox="0 0 56 60"><circle cx="28" cy="18" r="13" fill="#fff"/><path d="M13 18a15 15 0 0 1 30 0" fill="none" stroke="#fff" stroke-width="3"/><path d="M2 60a26 20 0 0 1 52 0z" fill="#fff"/></svg>
      <span>Request a call<br>back</span>
    </div>
    <label>I would like to discuss:</label>
    <div class="field" style="left:296px;top:97px;width:262px">Technology<svg style="position:absolute;right:14px;top:15px" width="9" height="6" viewBox="0 0 9 6"><path d="M0 0h9L4.5 6z" fill="#555"/></svg></div>
    <div class="field" style="left:581px;top:97px;width:262px">Name</div>
    <div class="field" style="left:296px;top:160px;width:262px">Phone no</div>
    <div class="submit">SUBMIT</div>
  </div>
</div>

<div class="section map" role="img" aria-label="Street map showing the office location with a red marker"></div>

<div class="section offices">
  <div class="wrap">
    <div class="office" style="left:10px">
      <h4>Head Office</h4>
      <div class="row"><svg viewBox="0 0 10 13"><path d="M5 0a4.5 4.5 0 0 0-4.5 4.5C.5 8 5 13 5 13s4.5-5 4.5-8.5A4.5 4.5 0 0 0 5 0z" fill="#fff"/></svg><span>48 Harbor Ave Suite 120<br>Eastfield, NJ 07000</span></div>
      <div class="row"><svg viewBox="0 0 12 12"><path d="M2.5 0l2 2.5-1.2 1.5a8 8 0 0 0 4.7 4.7L9.5 7.5 12 9.5 10.5 12C4.5 12 0 7.5 0 1.5z" fill="#fff"/></svg><span>+1 (555) 014 2200</span></div>
      <div class="row"><svg viewBox="0 0 12 12"><rect y="2" width="12" height="8" fill="#fff"/></svg><span>info@beaconadvisoryinc.example</span></div>
    </div>
    <div class="divider" style="left:256px"></div>
    <div class="office" style="left:304px">
      <h4>Technical Center</h4>
      <div class="row"><svg viewBox="0 0 10 13"><path d="M5 0a4.5 4.5 0 0 0-4.5 4.5C.5 8 5 13 5 13s4.5-5 4.5-8.5A4.5 4.5 0 0 0 5 0z" fill="#fff"/></svg><span>220 W Oak Road, Suite 300<br>Lakeview MI 48000</span></div>
      <div class="row"><svg viewBox="0 0 12 12"><path d="M2.5 0l2 2.5-1.2 1.5a8 8 0 0 0 4.7 4.7L9.5 7.5 12 9.5 10.5 12C4.5 12 0 7.5 0 1.5z" fill="#fff"/></svg><span>+1 (555) 014 2200</span></div>
      <div class="row"><svg viewBox="0 0 12 12"><rect y="2" width="12" height="8" fill="#fff"/></svg><span>tech@beaconadvisoryinc.example</span></div>
    </div>
    <div class="divider" style="left:552px"></div>
    <div class="office" style="left:594px">
      <h4>West Coast Office</h4>
      <div class="row"><svg viewBox="0 0 10 13"><path d="M5 0a4.5 4.5 0 0 0-4.5 4.5C.5 8 5 13 5 13s4.5-5 4.5-8.5A4.5 4.5 0 0 0 5 0z" fill="#fff"/></svg><span>910 Ridge Place, Suite 400<br>Westbay, CA 95000</span></div>
      <div class="row"><svg viewBox="0 0 12 12"><path d="M2.5 0l2 2.5-1.2 1.5a8 8 0 0 0 4.7 4.7L9.5 7.5 12 9.5 10.5 12C4.5 12 0 7.5 0 1.5z" fill="#fff"/></svg><span>+1 (555) 014 2200</span></div>
      <div class="row"><svg viewBox="0 0 12 12"><rect y="2" width="12" height="8" fill="#fff"/></svg><span>wc@beaconadvisoryinc.example</span></div>
    </div>
  </div>
</div>

<div class="section footer">
  <div class="wrap">
    <div class="logo"><span class="mark"></span>Beacon</div>
    <p class="about-text">Today's IT market is a dynamic, fast-paced industry, with ever-increasing demands. Meeting these demands for over 25 years, Beacon Advisory maintains a global presence, aggressively [...]</p>
    <div class="fcol" style="left:226px">
      <h5>Links</h5>
      <ul><li>Mission &amp; Vision</li><li>Focus</li><li>Services</li><li>Solutions</li><li>Our process</li><li>Staff Augmentation</li><li>Career</li></ul>
    </div>
    <div class="fcol" style="left:446px">
      <h5>FAQ</h5>
      <p style="padding-left:10px">So just what is the Beacon Advisory way?</p>
      <p style="margin-top:10px">Whether different industries, different financial concerns, different personalities [...]</p>
    </div>
    <div class="fcol" style="left:666px">
      <h5>Subscribe</h5>
      <div class="subscribe"><span>Email Id</span><b></b></div>
      <p style="margin-top:6px">Get latest updates</p>
    </div>
  </div>
</div>

<div class="section copy">
  <div class="wrap">
    <div class="text">Copyright © 2016 Beaconadvisoryinc</div>
    <div class="icons"><i></i><i></i><i></i><i></i></div>
  </div>
</div>

</body>
</html>
```